We are a new company with 2 divisions a medical research and medical product sales. We need a company logo and Business Cards. The design files need to be provided to us in Adobe Photoshop CS 5.1.

Target Market(s)

Medical Community

Industry/Entity Type

Medical

Contact Information for Business Card

Company Name - Harborline Biomedical LLC
Company Address 4150 SW 17th Ave Suite 8, Gainesville Fl 32611

Requirements
Must have
• The design files need to be provided to us in Adobe Photoshop CS 5.1.

```html
<!DOCTYPE html>
<html lang="en">
<head>
<meta charset="utf-8">
<title>Harborline Biomedical LLC – Business Cards</title>
<link href="https://fonts.googleapis.com/css2?family=Open+Sans:wght@400;600;700&display=swap" rel="stylesheet">
<style>
  :root {
    --page-bg: #eceef1;
    --card-white: #ffffff;
    --brand-blue: #1f6fc4;
    --band-blue-light: #3b8ddc;
    --band-blue-dark: #1a5aa8;
    --accent-red: #d6262b;
    --text-grey: #666a70;
    --rule-grey: #9a9ea4;
    --on-blue: #ffffff;
  }
  * { box-sizing: border-box; margin: 0; padding: 0; }
  html, body { width: 1200px; height: 784px; overflow: hidden; }
  body {
    background: var(--page-bg);
    font-family: "Open Sans", Arial, sans-serif;
    position: relative;
  }
  .card {
    position: absolute;
    width: 525px;
    height: 300px;
    background: var(--card-white);
    box-shadow: 0 6px 18px rgba(0,0,0,0.15);
    overflow: hidden;
  }
  .card--back { left: 50px; top: 242px; }
  .card--front { left: 625px; top: 242px; }

  /* Appointment side */
  .appt-title {
    position: absolute; top: 34px; left: 0; width: 100%;
    text-align: center; color: var(--brand-blue);
    font-size: 16px; font-weight: 600; text-decoration: underline;
  }
  .appt-field {
    position: absolute; display: flex; align-items: baseline;
    color: var(--text-grey); font-size: 14px; font-weight: 600;
  }
  .appt-field .dots {
    flex: 1; border-bottom: 2px dotted var(--rule-grey);
    margin-left: 6px; height: 1px;
  }
  .appt-name { left: 34px; top: 104px; width: 240px; }
  .appt-time { left: 290px; top: 94px; width: 200px; }
  .appt-date { left: 40px; top: 150px; width: 450px; }
  .appt-line-top {
    position: absolute; left: 260px; top: 60px; width: 230px;
    border-bottom: 2px dotted var(--rule-grey);
  }
  .brand-mark {
    position: absolute; display: flex; align-items: center; gap: 8px;
    color: var(--brand-blue); font-weight: 700; white-space: nowrap;
  }
  .brand-mark .dot {
    border-radius: 50%; background: var(--brand-blue); flex: none;
  }
  .card--back .brand-mark { right: 30px; bottom: 54px; font-size: 14px; }
  .card--back .brand-mark .dot { width: 18px; height: 18px; }

  /* Front side */
  .front-band { position: absolute; inset: 0; }
  .card--front .brand-mark {
    left: 0; right: 0; top: 70px; justify-content: center; font-size: 27px;
  }
  .card--front .brand-mark .dot { width: 30px; height: 30px; }
  .person {
    position: absolute; right: 285px; top: 218px; text-align: right;
  }
  .person-name { color: var(--accent-red); font-size: 17px; font-weight: 600; }
  .person-role { color: var(--on-blue); font-size: 13px; margin-top: 2px; }
  .divider {
    position: absolute; left: 256px; top: 200px; width: 1px; height: 78px;
    background: rgba(255,255,255,0.7);
  }
  .contact {
    position: absolute; left: 268px; top: 178px; list-style: none;
    color: var(--on-blue); font-size: 12px; line-height: 17px;
  }
  .contact li { display: flex; align-items: flex-start; gap: 6px; }
  .contact svg { width: 11px; height: 11px; margin-top: 3px; flex: none; }
</style>
</head>
<body>

<section class="card card--back" aria-label="Appointment card">
  <h2 class="appt-title">Appointments</h2>
  <div class="appt-line-top"></div>
  <div class="appt-field appt-name">Name :<span class="dots"></span></div>
  <div class="appt-field appt-time">Time :<span class="dots"></span></div>
  <div class="appt-field appt-date">Date :<span class="dots"></span></div>
  <div class="brand-mark"><span class="dot"></span>Harborline Biomedical LLC</div>
</section>

<section class="card card--front" aria-label="Business card">
  <svg class="front-band" viewBox="0 0 525 300" width="525" height="300" aria-hidden="true">
    <defs>
      <linearGradient id="bandGradient" x1="0" y1="0" x2="0" y2="1">
        <stop offset="0" stop-color="var(--band-blue-light)"/>
        <stop offset="1" stop-color="var(--band-blue-dark)"/>
      </linearGradient>
    </defs>
    <path d="M0 206 Q270 196 525 112 L525 300 L0 300 Z" fill="url(#bandGradient)"/>
    <path d="M0 203 Q270 193 525 109" fill="none" stroke="var(--accent-red)" stroke-width="2.5"/>
  </svg>

  <div class="brand-mark"><span class="dot"></span>Harborline Biomedical LLC</div>

  <div class="person">
    <div class="person-name">Dr. Elaine Corwell</div>
    <div class="person-role">Managing Director</div>
  </div>
  <div class="divider"></div>

  <ul class="contact">
    <li>
      <svg viewBox="0 0 12 12"><path d="M2.5 1 L4.5 1 L5.2 3.5 L4 4.5 Q5 7 7.5 8 L8.5 6.8 L11 7.5 L11 9.5 Q10 11 8.5 11 Q1 10 1 3.5 Q1 2 2.5 1Z" fill="var(--accent-red)"/></svg>
      <span>323-555-0142</span>
    </li>
    <li>
      <svg viewBox="0 0 12 12"><path d="M2.5 1 L4.5 1 L5.2 3.5 L4 4.5 Q5 7 7.5 8 L8.5 6.8 L11 7.5 L11 9.5 Q10 11 8.5 11 Q1 10 1 3.5 Q1 2 2.5 1Z" fill="var(--accent-red)"/></svg>
      <span>323-555-0187</span>
    </li>
    <li>
      <svg viewBox="0 0 12 12"><circle cx="6" cy="6" r="5" fill="none" stroke="var(--accent-red)" stroke-width="1.4"/><ellipse cx="6" cy="6" rx="2" ry="5" fill="none" stroke="var(--accent-red)" stroke-width="1.2"/><line x1="1" y1="6" x2="11" y2="6" stroke="var(--accent-red)" stroke-width="1.2"/></svg>
      <span>www.harborlinebio.com</span>
    </li>
    <li>
      <svg viewBox="0 0 12 12"><path d="M6 11 Q1.5 6.5 1.5 4.5 A4.5 4.5 0 0 1 10.5 4.5 Q10.5 6.5 6 11Z" fill="var(--accent-red)"/><circle cx="6" cy="4.5" r="1.6" fill="var(--on-blue)"/></svg>
      <span>4150 SW 17th Ave Suite 8,<br>Gainesville Fl 32611</span>
    </li>
  </ul>
</section>

</body>
</html>
```